Doctors clinic requires stationary designed

We require various types of stationary to be design based on the logo (attached). We require the following:
- Letterhead (A4 Portrait)
- Business Card (must include UV spot on rear)
- With compliments slip (DL Landscape)
- Appointments card (Folded A6)

We are a young clinical practice which boasts a modern and sophisticated approach to medicine so we require something which feels fresh and modern. Please include colours represented in the logo (contrasting teal and grey). We are calling for creative minds to put forth their ideas and we will be actively providing feedback on all designs.

thank you

Clinic

```html
<!DOCTYPE html>
<html lang="en">
<head>
<meta charset="utf-8">
<title>Dr Clara Whitmore – Letterhead</title>
<link rel="stylesheet" href="https://fonts.googleapis.com/css2?family=Source+Sans+3:wght@400;600&display=swap">
<style>
  :root {
    --teal: #1c9a89;
    --teal-soft: #e4f0ee;
    --grey: #8a9a98;
    --paper: #ffffff;
  }
  * { margin: 0; padding: 0; box-sizing: border-box; }
  html, body {
    width: 851px;
    height: 1200px;
    overflow: hidden;
    background: var(--paper);
  }
  .letterhead {
    position: relative;
    width: 851px;
    height: 1200px;
    background: var(--paper);
    font-family: "Source Sans 3", Arial, sans-serif;
  }
  .brand {
    position: absolute;
    top: 22px;
    left: 34px;
    display: flex;
    align-items: center;
    gap: 14px;
  }
  .brand-dot {
    width: 100px;
    height: 100px;
    border-radius: 50%;
    border: 4px solid var(--teal);
  }
  .brand-name {
    color: var(--teal);
    font-weight: 600;
    font-size: 40px;
    line-height: 1;
    letter-spacing: -0.5px;
  }
  .brand-role {
    margin-top: 4px;
    color: var(--teal);
    font-weight: 600;
    font-size: 20px;
    line-height: 1.1;
  }
  .header-rule {
    position: absolute;
    top: 108px;
    left: 147px;
    right: 20px;
    height: 2px;
    background: var(--teal-soft);
  }
  .decor-field {
    position: absolute;
    left: 268px;
    top: 586px;
    width: 522px;
    height: 570px;
    background: radial-gradient(ellipse at center, var(--teal-soft) 0%, rgba(228,240,238,0.55) 55%, rgba(255,255,255,0) 75%);
  }
</style>
</head>
<body>
  <main class="letterhead">
    <header class="brand">
      <div class="brand-dot"></div>
      <div class="brand-text">
        <div class="brand-name">Dr Clara Whitmore</div>
        <div class="brand-role">Obstetrician and Gynaecologist</div>
      </div>
    </header>
    <div class="header-rule"></div>
    <div class="decor-field" role="img" aria-label="Faint decorative clinic emblem watermark in pale teal"></div>
  </main>
</body>
</html>
```